Bright Builders WA Ball Poster

To Create a Poster for the Bright Builders WA Ball 2013

Target Market(s)

Young Professional Engineers aged 18-35. Male and Female

Requirements
Must have
• All Details required for the ball. Black and white/silver theme. Some kind of engineering theme. Must have the following text:

Join us in celebrating the Annual Bright Builders of Western Australia Ball with a night of dinner and entertainment.
Saturday July 13th, 2013
Time: 7pm Arrival
Venue: Corvane Ashby Hotel, Perth
Dress: Formal
The evening will include drinks, a three-course dinner, music and dancing.
Ticket price $139, on sale now! To purchase tickets go to:
(website to be announced)
Proceeds go to Makers Across Frontiers
is is an 18+ event. Open to general public.
Nice to have
• Modern, Classy, Similar to previous years designs. Possibly Masquerade themed.
Should not have
• Fish, environmental theme, rural Australia theme (these have been done)

```html
<!DOCTYPE html>
<html lang="en">
<head>
<meta charset="utf-8">
<title>Bright Builders WA Ball 2013</title>
<link rel="stylesheet" href="https://fonts.googleapis.com/css2?family=Great+Vibes&family=Raleway:wght@400;500;600;700&display=swap">
<style>
  :root {
    --night: #151515;
    --night-deep: #0a0a0a;
    --ink-light: #f2f2f2;
    --silver: #c4c4c4;
    --rule: #7a7a7a;
    --strip: #3a3a3a;
    --strip-text: #d8d8d8;
    --paper: #ffffff;
    --accent: #d8262b;
    --partner-ink: #1a1a1a;
    --green: #5aa02c;
  }
  * { margin: 0; padding: 0; box-sizing: border-box; }
  html, body { width: 1200px; height: 2412px; overflow: hidden; background: var(--night); }
  .poster {
    position: relative; width: 1200px; height: 2412px; overflow: hidden;
    background: radial-gradient(ellipse at 50% 45%, #262626 0%, var(--night) 55%, var(--night-deep) 100%);
    color: var(--ink-light);
    font-family: "Raleway", sans-serif;
  }
  .hero-suit {
    position: absolute; left: 0; top: 0; width: 1200px; height: 1020px;
    background:
      linear-gradient(180deg, rgba(21,21,21,0) 72%, var(--night) 100%),
      radial-gradient(ellipse 150px 640px at 50% 0%, #f6f6f6 0%, #e2e2e2 55%, rgba(40,40,40,0) 100%),
      linear-gradient(90deg, #080808 0%, #1c1c1c 30%, #2a2a2a 50%, #1c1c1c 70%, #080808 100%);
  }
  .invite { position: absolute; left: 0; width: 100%; text-align: center; }
  .kicker { top: 1046px; font-size: 28px; letter-spacing: 4px; font-weight: 500; color: var(--silver); }
  .title {
    top: 1090px; font-family: "Great Vibes", cursive; font-weight: 400;
    font-size: 88px; line-height: 84px; color: var(--ink-light);
  }
  .subline { top: 1276px; font-size: 28px; letter-spacing: 2px; font-weight: 500; color: var(--silver); }
  .host-mark {
    position: absolute; top: 1384px; left: 0; width: 100%;
    display: flex; justify-content: center; align-items: center; gap: 18px;
  }
  .host-mark .square { width: 76px; height: 76px; background: var(--accent); }
  .host-mark .name { font-size: 24px; font-weight: 600; letter-spacing: 1px; line-height: 28px; color: var(--ink-light); }
  .rule { position: absolute; left: 440px; width: 520px; height: 2px; background: var(--rule); }
  .rule.top { top: 1552px; }
  .rule.bottom { top: 1848px; }
  .details { position: absolute; top: 1600px; left: 0; width: 100%; text-align: center; font-size: 32px; line-height: 52px; letter-spacing: 1px; }
  .details .date { font-weight: 500; margin-bottom: 8px; }
  .details b { font-weight: 600; }
  .fine-print {
    position: absolute; top: 1950px; left: 60px; width: 1080px;
    font-size: 23px; line-height: 36px; color: var(--silver);
  }
  .fine-print p { margin-bottom: 40px; }
  .partner-strip {
    position: absolute; top: 2288px; left: 0; width: 100%; height: 36px;
    background: var(--strip); color: var(--strip-text);
    font-size: 16px; font-weight: 600; letter-spacing: 2px; line-height: 36px;
  }
  .partner-strip span { position: absolute; }
  .partner-strip .left { left: 60px; }
  .partner-strip .right { left: 460px; }
  .partner-row {
    position: absolute; top: 2324px; left: 0; width: 100%; height: 88px; background: var(--paper);
  }
  .partner {
    position: absolute; top: 50%; transform: translateY(-50%);
    display: flex; align-items: center; gap: 10px; color: var(--partner-ink); font-weight: 700;
  }
  .partner .dot { width: 36px; height: 36px; background: var(--green); }
  .partner .ring { width: 36px; height: 36px; border: 3px solid var(--green); border-radius: 50%; }
  .partner.lead { left: 60px; font-size: 44px; letter-spacing: 1px; }
  .partner.relief { left: 460px; font-size: 22px; }
  .partner.year { left: 740px; font-size: 20px; line-height: 24px; }
  .partner.frontiers { left: 930px; font-size: 20px; line-height: 24px; }
</style>
</head>
<body>
<main class="poster">
  <div class="hero-suit" role="img" aria-label="Photograph of a black tuxedo jacket with white shirt, studs and black bow tie"></div>

  <p class="invite kicker">JOIN US IN CELEBRATING</p>
  <h1 class="invite title">The Annual Bright Builders<br>of Western Australia Ball</h1>
  <p class="invite subline">WITH A NIGHT OF DINNER AND ENTERTAINMENT</p>

  <div class="host-mark">
    <span class="square"></span>
    <span class="name">CIVIC ENGINEERS GUILD<br>Bright Builders</span>
  </div>

  <div class="rule top"></div>
  <section class="details">
    <p class="date">SATURDAY JULY 13TH, 2013</p>
    <p><b>TIME:</b> 7pm Arrival</p>
    <p><b>VENUE:</b> Corvane Ashby Hotel, Perth</p>
    <p><b>DRESS:</b> Formal</p>
  </section>
  <div class="rule bottom"></div>

  <section class="fine-print">
    <p>The evening will include drinks, a three-course dinner, music and dancing.</p>
    <p>Ticket price $139, on sale now! To purchase tickets go to:<br>https://events.civicengineersguild.org.au</p>
    <p>Proceeds go to Makers Across Frontiers<br>Is an 18+ event. Open to general public.</p>
  </section>

  <div class="partner-strip">
    <span class="left">EVENT PARTNER</span>
    <span class="right">IN SUPPORT OF</span>
  </div>
  <div class="partner-row">
    <div class="partner lead">MERIDANE</div>
    <div class="partner relief"><span class="dot"></span>Kindwell Relief</div>
    <div class="partner year">Year of<br>Shared Works</div>
    <div class="partner frontiers"><span class="ring"></span>Makers Across<br>Frontiers</div>
  </div>
</main>
</body>
</html>
```